Welcome Email for new accounts

Dynamic welcome email for our new users who have signed up on our platform. Every time a new user creates an account, they will receive this email welcoming them. We really want it to be a personal welcome from our CEO.

Target Market(s)

Patients

Industry/Entity Type

Health And Wellness

Font styles to use
Serif

Requirements
Nice to have
• Lots of vector/graphics

```html
<!DOCTYPE html>
<html lang="en">
<head>
<meta charset="utf-8">
<title>Welcome to Healvia</title>
<link rel="stylesheet" href="https://fonts.googleapis.com/css2?family=Bodoni+Moda:wght@700;800&family=Open+Sans:ital,wght@0,400;0,600;1,400&display=swap">
<style>
:root{
  --page:#666666;
  --navy:#1f2541;
  --navy-soft:#2a3150;
  --coral:#e17462;
  --paper:#f6f6f6;
  --ink:#3d3d3d;
  --ink-dark:#1f2541;
  --white:#ffffff;
}
*{margin:0;padding:0;box-sizing:border-box}
html,body{width:729px;height:1200px;overflow:hidden}
body{background:var(--page);font-family:"Open Sans",sans-serif;color:var(--ink);position:relative}
.preheader,.unsubscribe{position:absolute;left:0;width:729px;text-align:center;font-size:8.5px;letter-spacing:2px;color:#e6e6e6;text-transform:uppercase}
.preheader{top:57px}
.unsubscribe{top:1135px}
.preheader a,.unsubscribe a{color:var(--coral);text-decoration:underline}
.email{position:absolute;left:137px;top:108px;width:455px;height:986px;background:var(--paper);box-shadow:0 0 24px rgba(0,0,0,.25)}
.hero{position:absolute;left:0;top:0;width:455px;height:276px}
.hero svg{display:block}
.brand{position:absolute;left:14px;top:24px;display:flex;align-items:center;gap:10px}
.brand-dot{width:50px;height:50px;border-radius:50%;background:var(--white)}
.brand-name{font-family:"Open Sans",sans-serif;font-weight:600;font-size:39px;color:var(--white);letter-spacing:.5px;line-height:1}
.content{position:absolute;left:12px;top:255px;width:430px}
.greeting{font-family:"Bodoni Moda",serif;font-weight:800;color:var(--ink-dark);font-size:24px;letter-spacing:1.5px;line-height:1.1}
.greeting-name{font-family:"Bodoni Moda",serif;font-weight:800;color:var(--coral);font-size:46px;letter-spacing:3px;line-height:1;margin-top:2px}
.intro{font-size:12.8px;line-height:18.2px;margin-top:7px}
.intro strong{font-weight:400;color:var(--ink-dark)}
.highlight{margin-top:18px;border-top:1.5px solid var(--coral);padding-top:2px}
.highlight p{background:var(--coral);color:var(--white);font-family:"Bodoni Moda",serif;font-weight:800;font-size:14.5px;letter-spacing:1.2px;line-height:18px;padding:7px 7px 8px}
.features{list-style:none;margin-top:13px}
.feature{display:flex;gap:14px;font-size:12.8px;line-height:16.7px;margin-bottom:18px}
.feature-icon{flex:none;width:27px;height:27px}
.signoff{margin-top:22px;font-size:12.8px;line-height:16.7px;padding-left:3px}
.signoff strong{font-weight:600;color:var(--ink-dark)}
.signature{margin-top:18px}
.signature em{font-style:italic}
.footer{position:absolute;left:0;top:828px;width:455px;height:131px;background:var(--navy);border-top:2px solid #d9d9d9;overflow:hidden;text-align:center;color:var(--white)}
.footer-mark{position:absolute;right:8px;top:6px;width:115px;height:115px;border-radius:50%;background:var(--navy-soft)}
.footer-url{position:relative;margin-top:20px;font-size:16.5px}
.social{position:relative;display:flex;justify-content:center;gap:5px;margin-top:8px}
.social span{width:22px;height:22px;border-radius:50%;background:var(--coral)}
.legal{position:relative;margin-top:12px;font-size:13px}
.legal span{margin:0 6px}
.copyright{position:absolute;left:0;top:959px;width:455px;height:27px;background:var(--coral);color:var(--white);text-align:center;font-size:13px;line-height:27px}
</style>
</head>
<body>
<p class="preheader">View this email on <a href="#">your browser</a></p>

<main class="email">
  <header class="hero">
    <svg width="455" height="276" viewBox="0 0 600 363" aria-hidden="true">
      <rect width="600" height="363" fill="#f6f6f6"/>
      <path d="M0,0 H600 V363 C560,358 535,305 495,300 C460,297 445,330 400,338 C340,348 300,318 235,262 C160,198 90,160 0,178 Z" fill="#1f2541"/>
    </svg>
    <div role="img" aria-label="Illustration of a white rocket launching with a coral flame, over faint medical icons" style="position:absolute;left:296px;top:18px;width:103px;height:205px;border-radius:50px 50px 40px 40px;background:linear-gradient(180deg,#e9e9ee 0%,#d6d6de 55%,#b0487a 72%,#e17462 100%)"></div>
    <div class="brand">
      <span class="brand-dot"></span>
      <span class="brand-name">healvia</span>
    </div>
  </header>

  <section class="content">
    <h1 class="greeting">Welcome to</h1>
    <p class="greeting-name">Healvia!</p>
    <p class="intro">You are now part of a community dedicated to better health! Instantly find Top-Rated Providers for Free. Verified Reviews. Search, Compare, Rate, and Schedule Care with <strong>Physicians, Dentists, Chiropractors, Acupuncturists, Nurse Practitioners, Counselors, and more</strong> on Healvia.</p>

    <div class="highlight"><p>With 3.2 million provider listings across the country, you’ll have the ability to:</p></div>

    <ul class="features">
      <li class="feature">
        <svg class="feature-icon" viewBox="0 0 28 28" aria-hidden="true"><circle cx="14" cy="14" r="13" fill="#1f2541"/><circle cx="14" cy="14" r="9" fill="#fff"/><path d="M9 12h9l-2-2M19 16h-9l2 2" stroke="#e17462" stroke-width="1.8" fill="none" stroke-linecap="round"/></svg>
        <span>Compare providers across practices and hospital affiliations.</span>
      </li>
      <li class="feature">
        <svg class="feature-icon" viewBox="0 0 28 28" aria-hidden="true"><circle cx="14" cy="14" r="13" fill="#1f2541"/><circle cx="14" cy="14" r="9" fill="#fff"/><circle cx="14" cy="14" r="5.5" fill="#e17462"/><path d="M11.5 14l2 2 3-3.5" stroke="#fff" stroke-width="1.5" fill="none"/></svg>
        <span>Make secure, real-time, medical appointment booking with automated appointment reminders and follow ups.</span>
      </li>
      <li class="feature">
        <svg class="feature-icon" viewBox="0 0 28 28" aria-hidden="true"><circle cx="14" cy="14" r="13" fill="#1f2541"/><circle cx="14" cy="14" r="9" fill="#fff"/><rect x="10" y="9" width="8" height="10" rx="1" fill="none" stroke="#e17462" stroke-width="1.4"/><path d="M12 12h4M12 14.5h4M12 17h2" stroke="#e17462" stroke-width="1.2"/></svg>
        <span>And search a review system that focuses on accountability. Customer reviews are based on each physician's National Provider Identifier (NPI) number, rather than just a physical address – so patients and providers can be assured that reviews are accurate and provider specific.</span>
      </li>
    </ul>

    <div class="signoff">
      <p>Thank you for becoming part of our community! If you have any questions or concerns, contact us at <strong>how@healvia.com.</strong></p>
      <p class="signature">Sincerely,<br><em>Marin Okafor</em><br>CEO</p>
    </div>
  </section>

  <footer class="footer">
    <span class="footer-mark"></span>
    <p class="footer-url">www.healvia.com</p>
    <div class="social" aria-label="Social links"><span></span><span></span><span></span></div>
    <p class="legal">Privacy Policy<span>|</span>Terms and Conditions<span>|</span>User Agreement</p>
  </footer>
  <p class="copyright">© 2020 Healvia Inc.</p>
</main>

<p class="unsubscribe">If you do not wish to receive future email, <a href="#">unsubscribe here</a></p>
</body>
</html>
```